Poster promoting the "Golden Crust Day"

The Meridan Federation of Oven Crafts (MFOC) created the "Golden Crust Day" in 2006. It is celebreated each year together with the GNX "Harvest Table Day" on 16th October.
After using different posters for a few years, MFOC decided to settle on a permanent poster some time ago, in order to allow people to recognize the poster long-term.
Now, MFOC feels that this permanent poster needs an update and modernization, apart from including the new MFOC logo.
Requisits:
1. Must include the new MFOC logo
2. The poster should reflect the importance of bread in the world and convey an image of health, innovation and tradition.
3. One version with text, one version without text
4. Text version: one poster for each of the four official MFOC languages:
ENGLISH: Golden Crust Day / 16th October
GERMAN: Goldkrustentag / 16. Oktober
SPANISH: Día de la Corteza Dorada / 16 de Octubre
FRENCH: Journée de la Croûte Dorée / 16 Octobre
5. Colours must be defined with RGB colour code.
MFOC will take a decision regarding the new poster design during the next meeting of its Marketing Commission on March 24th, 2015. Therefore, please submit your proposals by 18th March in order to allow for pre-selection and modification requests.
More about MFOC at www.meridanovencrafts.org.

```html
<!DOCTYPE html>
<html lang="en">
<head>
<meta charset="utf-8">
<title>Golden Crust Day — Poster</title>
<link rel="stylesheet" href="https://fonts.googleapis.com/css2?family=Cinzel:wght@400;500&family=Montserrat:wght@400;700&display=swap">
<style>
  :root {
    --backdrop: #dfe5ea;
    --paper: #f3ede1;
    --crimson: #8a1a1c;
    --crimson-deep: #6e1214;
    --amber: #e39a2d;
    --crust-light: #f0c27a;
    --crust-dark: #b8702c;
  }
  * { margin: 0; padding: 0; box-sizing: border-box; }
  html, body {
    width: 1200px;
    height: 960px;
    overflow: hidden;
    background: var(--backdrop);
  }
  .poster {
    position: absolute;
    left: 280px;
    top: 30px;
    width: 640px;
    height: 900px;
    background: var(--paper);
    color: var(--crimson);
  }
  .brand {
    position: absolute;
    left: 26px;
    top: 34px;
    display: flex;
    align-items: center;
    gap: 10px;
  }
  .brand-dot {
    width: 22px;
    height: 22px;
    border-radius: 50%;
    background: var(--amber);
  }
  .brand-name {
    font-family: "Montserrat", sans-serif;
    font-weight: 400;
    font-size: 34px;
    color: var(--crimson);
    letter-spacing: 1px;
  }
  .globe-artwork {
    position: absolute;
    left: 76px;
    top: 82px;
    width: 490px;
    height: 490px;
  }
  .title {
    position: absolute;
    left: 0;
    right: 0;
    top: 612px;
    text-align: center;
    font-family: "Cinzel", serif;
    font-weight: 400;
    color: var(--crimson);
    line-height: 1;
  }
  .title-top {
    display: block;
    font-size: 54px;
    letter-spacing: 1px;
  }
  .title-main {
    display: block;
    font-size: 118px;
    margin-top: 2px;
    letter-spacing: 2px;
  }
  .date-line {
    position: absolute;
    left: 0;
    right: 0;
    top: 798px;
    display: flex;
    justify-content: center;
    align-items: center;
    gap: 14px;
  }
  .date-bar {
    width: 82px;
    height: 8px;
    background: var(--amber);
  }
  .date-text {
    font-family: "Montserrat", sans-serif;
    font-weight: 700;
    font-size: 23px;
    letter-spacing: 1px;
    color: var(--crimson);
  }
  .date-text sup { font-size: 13px; vertical-align: 9px; }
  .website {
    position: absolute;
    left: 0;
    right: 0;
    top: 846px;
    text-align: center;
    font-family: "Montserrat", sans-serif;
    font-weight: 400;
    font-size: 18px;
    color: var(--crimson);
  }
</style>
</head>
<body>
  <main class="poster">
    <div class="brand">
      <span class="brand-dot"></span>
      <span class="brand-name">mfoc</span>
    </div>

    <svg class="globe-artwork" viewBox="0 0 490 490" role="img" aria-label="Globe with crimson continents, the oceans filled with an assortment of breads, bagels and loaves">
      <defs>
        <radialGradient id="globe-fill" cx="45%" cy="40%" r="60%">
          <stop offset="0%" stop-color="#a8322e"/>
          <stop offset="55%" stop-color="var(--crimson)"/>
          <stop offset="100%" stop-color="#c47a3c"/>
        </radialGradient>
      </defs>
      <circle cx="245" cy="245" r="240" fill="url(#globe-fill)"/>
    </svg>

    <h1 class="title">
      <span class="title-top">GOLDEN CRUST</span>
      <span class="title-main">DAY</span>
    </h1>

    <div class="date-line">
      <span class="date-bar"></span>
      <span class="date-text">16<sup>TH</sup> OCTOBER</span>
      <span class="date-bar"></span>
    </div>

    <p class="website">meridanovencrafts.org</p>
  </main>
</body>
</html>
```